Paths to Delight E-card design - Potential for other work

I am looking for a designer to create e card, thank you design templates for my new not for profit website www.pathstodelight.com.au.

They will have simple imagery, with a subtle and soft illustration which reflects some sort of emotion. Think of patterns and textures.

The main focus of the card will be the text submitted as the "Path to Delight". For an example of the text please see http://www.pathstodelight.com.au/search-for-ideas/.

The width of the card / image (which will be displayed on a web page) will be 700px max, and there is no restriction on height.

The colours will be similar to the website colours although possibly softer/pastal colours.

The design should contain a header/title "You've amazed me, thank you" before the actual words merged from the site as the Path to Delight. It will appear on a blank page on the website with the same header so it doesn't have to be similar to the website design.

I will upload similar designs I like to make your job easier on Monday.

Although this job is only for a couple of simple designs, I will require more in the future so there is potential for ongoing work. I am therefore looking for a provider who is reliable, trustworthy, efficient and of course has a creative design flair.

If you want to be a part of a great cause, please submit your designs. I look forward to working with you.

Thank you.

Target Market(s)

Everyone with a kind heart ;0)

Industry/Entity Type

Work

Requirements
Nice to have
• In terms of the attached files, 1 and 2 give an example of a pattern that is quite nice. Number 4 shows the colours I quite like with the orange. We want the e card to evoke emotion. (please note the design Is for an e card, not business card. This is just an example of a design, please ignore the fact it is on a business card.
Should not have
• Too much going on

```html
<!DOCTYPE html>
<html lang="en">
<head>
<meta charset="utf-8">
<title>Chocolate for a Friend in need – Paths to Delight e-card</title>
<link rel="stylesheet" href="https://fonts.googleapis.com/css2?family=Varela+Round&display=swap">
<style>
  :root {
    --card-orange: #ff9a5e;
    --string: #5b3a2c;
    --panel: #eeeeee;
    --title-pill: #f0f0f0;
    --ink: #3b3b3b;
    --brand-orange: #f26a1f;
    --white: #ffffff;
    --shadow: rgba(150, 70, 20, 0.35);
  }
  * { box-sizing: border-box; margin: 0; padding: 0; }
  html, body {
    width: 1200px;
    height: 857px;
    overflow: hidden;
    background: var(--card-orange);
  }
  .ecard {
    position: relative;
    width: 1200px;
    height: 857px;
    background: var(--card-orange);
    font-family: "Varela Round", Arial, sans-serif;
    color: var(--ink);
  }
  .swatch-strip {
    position: absolute;
    top: 0; left: 0;
    width: 100%;
    height: 17px;
    display: flex;
  }
  .swatch-strip span { flex: 1; }
  .hanging-string {
    position: absolute;
    top: 17px;
    width: 3px;
    height: 270px;
    background: var(--string);
  }
  .hanging-string--left { left: 256px; }
  .hanging-string--right { left: 959px; }
  .title-pill {
    position: absolute;
    left: 117px;
    top: 108px;
    width: 973px;
    height: 104px;
    border-radius: 52px;
    background: var(--title-pill);
    box-shadow: 0 7px 0 var(--shadow);
    transform: rotate(-3deg);
    display: flex;
    align-items: center;
    justify-content: center;
  }
  .title-pill h1 {
    font-weight: 400;
    font-size: 55px;
    letter-spacing: 0.5px;
    color: var(--ink);
  }
  .story-panel {
    position: absolute;
    left: 117px;
    top: 283px;
    width: 973px;
    height: 480px;
    border-radius: 26px;
    background: var(--panel);
    box-shadow: 0 7px 0 var(--shadow);
    padding: 70px 70px 0;
  }
  .story-panel p {
    font-size: 30px;
    line-height: 42px;
    text-align: center;
    color: var(--ink);
  }
  .brand-badge {
    position: absolute;
    left: 908px;
    top: 703px;
    width: 224px;
    height: 114px;
    border-radius: 14px;
    background: var(--brand-orange);
    border: 4px solid var(--white);
    box-shadow: 0 5px 0 var(--shadow);
    display: flex;
    align-items: center;
    justify-content: center;
    text-align: center;
  }
  .brand-badge span {
    font-size: 30px;
    line-height: 34px;
    color: var(--white);
  }
</style>
</head>
<body>
<main class="ecard">
  <div class="swatch-strip" aria-hidden="true">
    <span style="background:#8ea7a6"></span>
    <span style="background:#a3b5b1"></span>
    <span style="background:#d9d4b2"></span>
    <span style="background:#d9c866"></span>
    <span style="background:#e3d283"></span>
    <span style="background:#c9c49c"></span>
    <span style="background:#a6b37e"></span>
    <span style="background:#c7b08e"></span>
    <span style="background:#b6a88e"></span>
    <span style="background:#f4d46c"></span>
    <span style="background:#f8cd62"></span>
    <span style="background:#f5d79f"></span>
    <span style="background:#f2a17b"></span>
    <span style="background:#f59a84"></span>
    <span style="background:#f7b799"></span>
    <span style="background:#f8c6a9"></span>
    <span style="background:#d98a8a"></span>
    <span style="background:#e07a8c"></span>
    <span style="background:#f3a5a5"></span>
    <span style="background:#f8c1b8"></span>
  </div>

  <div class="hanging-string hanging-string--left" aria-hidden="true"></div>
  <div class="hanging-string hanging-string--right" aria-hidden="true"></div>

  <header class="title-pill">
    <h1>Chocolate for a Friend in need</h1>
  </header>

  <section class="story-panel">
    <p>My friend had recently broke up with her longterm boyfriend and was quite upset (although she was looking on the bright side – she could find someone much better suited!) So I sent her a bag of Harlow's chocolate freckles and chocolate biscuit. And she loved it! Although it didn't cost me much, it brought a smile to her face when she needed it, and showed her that she has friends around her that care about her and love her.</p>
  </section>

  <div class="brand-badge">
    <span>Paths to Delight</span>
  </div>
</main>
</body>
</html>
```